Australia's newest tech recruitment startup

We are a new tech startup in the recruitment space.

We leverage the existing infrastructure of the recruitment network and bundle a value market based business model (like brisk fennel) that appeals to business.

We are very individual, afraid of no one, minimalist, and defiantly NO "BS"!!

We're not cut price think Vantor Hale rather than Kesumi
Updates

Hey Everyone,

thanks so much for your designs. I have eliminated a lot of designs but if I havent to yours then your in with a shot. I would like to see the designs updated with a spot for our twitter handle, my blog address & our linkedIn group address. 

For some designs I think some of the above would look ok on the back of the card so not to make the front look too messy. 

thanks   

Target Market(s)

Our target market is SME's young baby boomer and Gen X

Industry/Entity Type

Business

Requirements
Must have
• Company logo, doesn't have to be both

```html
<!DOCTYPE html>
<html lang="en">
<head>
<meta charset="utf-8">
<title>Brightpath Hire – Business Cards</title>
<link rel="stylesheet" href="https://fonts.googleapis.com/css2?family=Open+Sans:wght@400;600;700&display=swap">
<style>
  :root {
    --bg: #f1f1f1;
    --brand-blue: #0aa9de;
    --brand-blue-light: #19b3e6;
    --card-white: #ffffff;
    --band-grey: #d9d9d9;
    --name-grey: #f0f0f0;
    --ink: #444444;
    --on-blue: #ffffff;
  }
  * { box-sizing: border-box; margin: 0; padding: 0; }
  html, body {
    width: 1200px;
    height: 741px;
    overflow: hidden;
    background: var(--bg);
    font-family: "Open Sans", Arial, sans-serif;
  }
  .canvas {
    position: relative;
    width: 1200px;
    height: 741px;
    display: flex;
    align-items: center;
    justify-content: center;
    gap: 40px;
  }
  .card {
    position: relative;
    width: 520px;
    height: 290px;
    overflow: hidden;
    box-shadow: 0 6px 18px rgba(0,0,0,0.12);
  }

  /* Front */
  .card--front { background: var(--card-white); }
  .front__logo-zone {
    position: absolute;
    left: 0; top: 0;
    width: 100%; height: 150px;
    display: flex;
    align-items: center;
    justify-content: center;
    gap: 14px;
  }
  .wordmark {
    font-weight: 700;
    font-size: 54px;
    letter-spacing: -1px;
    color: var(--brand-blue);
    line-height: 1;
  }
  .wordmark-dot {
    width: 16px; height: 16px;
    border-radius: 50%;
    background: var(--brand-blue);
  }
  .front__band {
    position: absolute;
    left: 0; top: 150px;
    width: 100%; height: 14px;
    background: var(--band-grey);
  }
  .front__name-zone {
    position: absolute;
    left: 0; top: 164px;
    width: 100%; height: 42px;
    background: var(--name-grey);
    display: flex;
    align-items: center;
    justify-content: center;
    color: var(--ink);
  }
  .holder-name { font-weight: 700; font-size: 17px; }
  .holder-title { font-weight: 400; font-size: 12px; margin-left: 5px; }
  .front__rule {
    position: absolute;
    left: 0; top: 206px;
    width: 100%; height: 6px;
    background: var(--band-grey);
  }
  .front__contact {
    position: absolute;
    left: 0; top: 212px;
    width: 100%; height: 78px;
    background: var(--brand-blue);
    color: var(--on-blue);
    display: flex;
    flex-direction: column;
    align-items: center;
    justify-content: center;
    gap: 9px;
  }
  .contact-line {
    display: flex;
    align-items: center;
    gap: 14px;
    font-size: 13px;
  }
  .contact-item { display: flex; align-items: center; gap: 5px; }
  .contact-icon { width: 12px; height: 12px; }
  .website {
    font-size: 12px;
    letter-spacing: 4.5px;
  }

  /* Back */
  .card--back { background: var(--brand-blue); }
  .back__panel {
    position: absolute;
    left: 42px; top: 70px;
    width: 436px; height: 150px;
    background: var(--brand-blue-light);
    display: flex;
    align-items: center;
    justify-content: center;
    gap: 14px;
  }
  .back__panel .wordmark { color: var(--on-blue); font-size: 52px; }
  .back__panel .wordmark-dot { background: var(--on-blue); }
</style>
</head>
<body>
<main class="canvas">

  <section class="card card--front" aria-label="Business card front">
    <div class="front__logo-zone">
      <span class="wordmark">Brightpath Hire</span>
      <span class="wordmark-dot"></span>
    </div>
    <div class="front__band"></div>
    <div class="front__name-zone">
      <span class="holder-name">Your Name,</span><span class="holder-title">Title</span>
    </div>
    <div class="front__rule"></div>
    <div class="front__contact">
      <div class="contact-line">
        <span class="contact-item">
          <svg class="contact-icon" viewBox="0 0 12 12" aria-hidden="true">
            <path d="M3 1.2 L4.6 3.6 L3.6 4.8 Q4.6 7 7.2 8.4 L8.4 7.4 L10.8 9 L9.8 10.8 Q5.6 10.6 2.4 7 Q0.8 4.6 1.2 2.2 Z" fill="#ffffff"/>
          </svg>
          0400 318 762
        </span>
        <span class="contact-item">
          <svg class="contact-icon" viewBox="0 0 12 12" aria-hidden="true">
            <rect x="1" y="3" width="10" height="7" rx="1" fill="#ffffff"/>
            <path d="M1.5 3.5 L6 7 L10.5 3.5" fill="none" stroke="#0aa9de" stroke-width="1"/>
          </svg>
          info@brightpathhire.com.au
        </span>
      </div>
      <div class="website">www.brightpathhire.com.au</div>
    </div>
  </section>

  <section class="card card--back" aria-label="Business card back">
    <div class="back__panel">
      <span class="wordmark">Brightpath Hire</span>
      <span class="wordmark-dot"></span>
    </div>
  </section>

</main>
</body>
</html>
```